Wordpress Identity for Innovation Firm

Copper Lantern Partners is an innovation and investment firm based in Los Angeles.

We are seeking a designer that can help create our company identity and Wordpress site.

The attached Design Brief provides more details.

Designers Responsibility:

1) Company Identity

The designer will create the company identity.
Attached is a file that contains a type font that I like a lot.
No logo design is required.

The Copper Lantern Partners type font should become the company identity.
The attached document provides an overview of company type font identities that we like.

2) Wordpress Theme & Design

The designer will select existing Wordpress Themes that meet our design desires, and present them as part of the design proposal.

We will make our selection based on the selected Wordpress Theme(s), which the designer will creatively adapt with the new company identity.

Target Market(s)

We anticipate the website being mostly accessed by the US, Canada and European countries.

Our target audience includes the following:

• Corporations, companies, startups, non-profits
• Banks, venture capital, private equity, investors
• Incubators, accelerators, innovation clusters, research labs, universities
• Ad agencies, marketing agencies, digital agencies, media, press

Industry/Entity Type

Investment

Number of Pages Required

1 page

Font styles to use
Sans Serif
Other font styles liked:
• See attached design brief materials. The Font will represent the brand identity!

Requirements
Must have
• The ability to scroll through information top to bottom is important to us.
• This is in line with today's Wordpress themes.
• The website must be able to function across devices (desktop, tablet, phone).
• The top 5 web browsers and platforms (Mac/PC/Android/iOS)
• Contact us link or information field
Nice to have
• It would be nice to have a moving image in the background, such as:
• https://drifttrial.sitehatch.com
• The Wordpress theme of the moving image or video should be relevant to our overall Technology Innovation theme.
• Key words:
• Technology Innovation
• Digital
• Business
• Transportation
• Advanced Vehicles (auto, boat, airplane, rail, space)
• Space
• Venture Capital
• Investing
Should not have
• eCommerce

```html
<!DOCTYPE html>
<html lang="en">
<head>
<meta charset="utf-8">
<title>Copper Lantern Partners</title>
<link href="https://fonts.googleapis.com/css2?family=Open+Sans:wght@400;600;700&family=Raleway:wght@400;600;700&display=swap" rel="stylesheet">
<style>
:root{
  --ink:#222;
  --text:#555;
  --muted:#888;
  --rule:#d8d8d8;
  --paper:#fff;
  --dark:#222;
  --darker:#181818;
  --light:#fff;
}
*{box-sizing:border-box;margin:0;padding:0}
html,body{width:1200px;height:2200px;overflow:hidden;background:var(--paper)}
body{font-family:"Open Sans",Arial,sans-serif;color:var(--text);position:relative}
.hero{position:absolute;top:0;left:0;width:1200px;height:552px;
  background:radial-gradient(ellipse at 55% 35%,#9a9a9a 0%,#6e6e6e 45%,#3c3c3c 100%)}
.site-header{position:absolute;top:0;left:0;width:100%;height:80px;display:flex;align-items:center;justify-content:space-between;padding:0 36px}
.brand{font-family:"Raleway",Arial,sans-serif;font-weight:600;font-size:28px;color:var(--light)}
.menu-toggle{width:26px;height:20px;display:flex;flex-direction:column;justify-content:space-between}
.menu-toggle span{height:3px;background:var(--light)}
.hero-text{position:absolute;top:262px;left:0;width:100%;text-align:center;color:var(--light);font-family:"Raleway",Arial,sans-serif}
.hero-text .line1{font-size:32px;font-weight:400}
.hero-text .amp{font-size:26px;font-weight:700;margin:8px 0}
.hero-text .line2{font-size:30px;font-weight:600;letter-spacing:1px}
.hero-arrow{position:absolute;top:264px;width:28px;height:28px}
.hero-arrow.prev{left:22px}.hero-arrow.next{right:22px}
.section-title{font-family:"Raleway",Arial,sans-serif;font-weight:700;font-size:20px;color:var(--ink);letter-spacing:.5px}
.section-sub{font-size:9px;color:var(--muted);letter-spacing:.6px;margin-top:10px}
.btn{display:inline-block;border:2px solid var(--ink);padding:7px 22px;font-size:10px;font-weight:700;color:var(--ink);letter-spacing:.5px}
.about{position:absolute;top:552px;left:0;width:100%;height:320px;text-align:center;padding-top:52px}
.about p{width:900px;margin:30px auto 0;font-size:11px;line-height:21px;color:var(--text)}
.about .btn{margin-top:28px}
.divider{position:absolute;top:872px;left:96px;width:1008px;border-top:1px solid var(--rule)}
.services{position:absolute;top:910px;left:96px;width:1008px}
.cards{display:flex;justify-content:space-between;margin-top:42px}
.card{width:480px}
.card .photo{height:228px}
.card h3{font-size:10px;font-weight:700;color:var(--ink);margin-top:24px;letter-spacing:.4px}
.card p{font-size:10px;line-height:17px;margin-top:10px;color:var(--text);width:460px}
.card .btn{margin-top:22px}
.photo-meeting{background:linear-gradient(180deg,#e9e9e9 0%,#bdbdbd 60%,#6a6a6a 100%)}
.photo-coins{background:linear-gradient(180deg,#f2f2f2 0%,#cfcfcf 50%,#8a8a8a 100%)}
.portfolio{position:absolute;top:1464px;left:0;width:100%;height:344px;background:var(--dark);text-align:center;padding-top:48px}
.portfolio .section-title{color:var(--light);font-size:18px}
.tiles{position:absolute;top:128px;left:104px;width:996px;height:184px;display:flex}
.tile{flex:1;height:100%;position:relative}
.tile.t1{background:linear-gradient(135deg,#5a5a5a,#2e2e2e)}
.tile.t2{background:linear-gradient(160deg,#d8d8d8,#7a7a7a)}
.tile.t3{background:linear-gradient(150deg,#bcbcbc,#4d4d4d)}
.tile.t4{background:linear-gradient(170deg,#e0e0e0,#5e5e5e)}
.tile-overlay{position:absolute;inset:0;background:rgba(20,20,20,.55);text-align:left;padding:30px 0 0 18px;color:var(--light)}
.tile-overlay strong{display:block;font-size:10px;font-weight:700;letter-spacing:.4px}
.tile-overlay span{font-size:8px;color:#ccc}
.customers{position:absolute;top:1872px;left:0;width:100%;text-align:center}
.customers .section-title{font-size:18px}
.clients{display:flex;justify-content:space-between;align-items:center;width:1036px;margin:56px auto 0}
.client{font-family:"Open Sans",Arial,sans-serif;font-weight:600;font-size:22px;color:#444}
.site-footer{position:absolute;top:2100px;left:0;width:100%;height:100px;background:var(--darker);display:flex;align-items:center;justify-content:space-between;padding:0 26px}
.copyright{font-size:8px;color:#999;letter-spacing:.4px}
.connect{display:flex;align-items:center;gap:16px;font-size:8px;color:#999;letter-spacing:.4px}
.connect i{width:16px;height:16px;border-radius:50%;background:#bbb;display:block}
</style>
</head>
<body>
<section class="hero" role="img" aria-label="Grey-toned photo of a hand holding a glowing bar chart over a business desk">
  <header class="site-header">
    <div class="brand">Copper Lantern Partners</div>
    <div class="menu-toggle"><span></span><span></span><span></span></div>
  </header>
  <svg class="hero-arrow prev" viewBox="0 0 28 28"><circle cx="14" cy="14" r="13" fill="rgba(255,255,255,.25)"/><path d="M16 8l-6 6 6 6" stroke="#fff" stroke-width="2" fill="none"/></svg>
  <svg class="hero-arrow next" viewBox="0 0 28 28"><circle cx="14" cy="14" r="13" fill="rgba(255,255,255,.25)"/><path d="M12 8l6 6-6 6" stroke="#fff" stroke-width="2" fill="none"/></svg>
  <div class="hero-text">
    <div class="line1">Copper Lantern Partners is an innovation</div>
    <div class="amp">&amp;</div>
    <div class="line2">INVESTMENT FIRM</div>
  </div>
</section>

<section class="about">
  <h2 class="section-title">ABOUT THE COMPANY</h2>
  <div class="section-sub">COPPER LANTERN PARTNERS IS AN INNOVATION COMPANY BASED IN LOS ANGELES</div>
  <p>We back bold founders who turn new technology into lasting business value. From early research to global scale, our team brings capital, strategy and a network of partners across transportation, space, digital media and advanced vehicles. We help ideas move faster from the lab to the market, and we stay close to every company we support.</p>
  <span class="btn">VIEW MORE</span>
</section>

<div class="divider"></div>

<section class="services">
  <h2 class="section-title">PRODUCTS &amp; SERVICES</h2>
  <div class="section-sub">NEQUE PORRO QUISQUAM EST QUI DOLOREM IPSUM QUIA DOLOR SIT AMET, CONSECTETUR, ADIPISCI VELIT, SED QUIA</div>
  <div class="cards">
    <article class="card">
      <div class="photo photo-meeting" role="img" aria-label="Business people shaking hands in a bright office"></div>
      <h3>BUILD DIGITAL COMPANIES</h3>
      <p>Capital and guidance for digital ventures, from first prototype to market launch and growth across new regions and sectors.</p>
      <span class="btn">VIEW MORE</span>
    </article>
    <article class="card">
      <div class="photo photo-coins" role="img" aria-label="Stacks of coins on a desk"></div>
      <h3>SUPPORT EUROPEAN</h3>
      <p>Partnering with European founders to scale research labs and startups into strong companies with lasting reach worldwide.</p>
      <span class="btn">VIEW MORE</span>
    </article>
  </div>
</section>

<section class="portfolio">
  <h2 class="section-title">PORTFOLIO</h2>
  <div class="tiles">
    <div class="tile t1" role="img" aria-label="Portfolio project image">
      <div class="tile-overlay"><strong>VENTURE ONE</strong><span>Digital</span></div>
    </div>
    <div class="tile t2" role="img" aria-label="Hands holding a young plant"></div>
    <div class="tile t3" role="img" aria-label="Close-up of financial charts"></div>
    <div class="tile t4" role="img" aria-label="Businessman standing beside rising bars"></div>
  </div>
</section>

<section class="customers">
  <h2 class="section-title">CUSTOMERS</h2>
  <div class="section-sub">NEQUE PORRO QUISQUAM EST QUI DOLOREM IPSUM QUIA DOLOR SIT AMET, CONSECTETUR, ADIPISCI VELIT, SED QUIA</div>
  <div class="clients">
    <span class="client">Arcway</span>
    <span class="client">Fernlux</span>
    <span class="client">Glimmo</span>
    <span class="client">Halden Row</span>
    <span class="client">Orla Finch</span>
    <span class="client">Nordvik</span>
  </div>
</section>

<footer class="site-footer">
  <div class="copyright">© 2024 COPPER LANTERN PARTNERS. ALL RIGHTS RESERVED.</div>
  <div class="connect">CONNECT WITH US <i></i><i></i><i></i><i></i></div>
</footer>
</body>
</html>
```